Mobile App design improvement- Figma

I have four screens need to redesign, and I have the design guide to help you.
The goal is to make the design clean and easy to understand CTA improve UI/UX. You can change the icons, and don't change the fonts or color. Also, if you are doing a great job, I will hire you finish the rest of the design of the app.
Here is our site: https://pelvosta.com
Pelvosta App is wishlist:
Hight features and app propositions of the app collaborative shopping and chatting with invited friends and family. Easily to get feedback and make decisions of the products from friends, chat, vote, poll, compare.
Here is the Figma link: https://www.example-design.com/design/Kx7Tq2LmWz9PbNv4HdYsRe/Pelvosta--App?node-id=31-47215&t=Jq8WmZr3VxNt5KpLa-7
Here is the app links:
IOS app:
https://lnkhop.io/8KqTz2m

Android app:
https://lnkhop.io/8KqTz2p
Updates

1. I need to have more design ideas that makes users feel simple and easy to understudy platforms can add products from search products, paste url, and use share button to add proton there wishlist from other e-commerce sites. Simplify the search, paste url, and user share button page, maybe combine search with paste url in the search bar, or switch back and forth with search key, paste URL, or share product from other e-commerce sites. Shop page, maybe show users to pick favorites brands recommended products and popular brands. My profile page, I need to be simple but also give users ability to navigate between the save money and wishlists. Please don’t change my color of the app header and color theme. Tone: Ecommerce marketplace, social media, fun! Highlights invite friends chat, save money, and add product.

Target Market(s)

female CEOs, moms, female interns

Industry/Entity Type

Social networking, shopping.

Number of Pages Required

4 page

Font styles to use
Other font styles liked:
• please look at our brand guide

Requirements
Nice to have
• Simple design, highlight invite memebers, and highlight 3 options for them to get products into one place. Highlight collabrative and social tone.
Should not have
• Don't give me too much colors.

```html
<!DOCTYPE html>
<html lang="en">
<head>
<meta charset="utf-8">
<title>Pelvosta App – Screens</title>
<link href="https://fonts.googleapis.com/css2?family=Montserrat:ital,wght@0,400;0,500;0,600;0,700;1,400&display=swap" rel="stylesheet">
<style>
:root{
  --purple:#4436cb;
  --lime:#a6e83a;
  --teal:#5fead8;
  --teal-soft:#dbfaf4;
  --lavender:#ecebfa;
  --board:#cacaca;
  --white:#ffffff;
  --ink:#111111;
  --muted:#555555;
  --shoe-a:#5b7fb8;
  --shoe-b:#2c4f86;
  --cake-a:#8fc2d6;
  --cake-b:#3f6f86;
}
*{box-sizing:border-box;margin:0;padding:0}
html,body{width:1200px;height:574px;overflow:hidden}
body{background:var(--board);font-family:"Montserrat",sans-serif;color:var(--ink);position:relative}
.screen{position:absolute;transform-origin:0 0;transform:scale(.4658);background:var(--white);overflow:hidden}
.screen > *{position:absolute}
.icon{fill:none;stroke:currentColor;stroke-width:2;stroke-linecap:round;stroke-linejoin:round}

/* header */
.app-header{left:0;top:0;width:100%;background:var(--purple);color:var(--white);display:flex;align-items:center}
.app-header .back{width:26px;height:26px;margin-left:20px}
.app-header h1{font-weight:700;font-size:20px;margin-left:14px;letter-spacing:.2px}
.header-avatar{position:absolute;border-radius:50%;background:radial-gradient(circle at 50% 40%,#c9a58c,#4a3a33)}

/* profile */
.lavender{left:0;width:100%;background:var(--lavender)}
.avatar{border-radius:50%;background:radial-gradient(circle at 50% 42%,#d1ad93 0 35%,#5b4a40 70%,#c9c9c9)}
.name{font-weight:700}
.edit{background:var(--lime);font-weight:500;display:flex;align-items:center;justify-content:center}
.stat{background:var(--white);display:flex;flex-direction:column;align-items:center;justify-content:center}
.stat b{color:var(--purple);font-weight:700}
.tabs{left:0;width:100%;display:flex;font-weight:700}
.tabs div{display:flex;align-items:center;justify-content:center}
.tab-on{background:var(--lime);color:var(--ink)}
.tab-off{background:var(--purple);color:var(--white);flex:1}
.wishlist-card{background:linear-gradient(160deg,var(--cake-a),var(--cake-b))}
.wishlist-card .members{position:absolute;left:0;background:var(--white)}
.wishlist-card .lock{position:absolute;color:var(--white)}
.wishlist-card .title{position:absolute;color:var(--white);font-weight:500}

/* tab bar */
.tabbar{left:0;bottom:0;width:100%;background:var(--purple);display:grid;color:var(--white)}
.tabbar a{display:flex;flex-direction:column;align-items:center;justify-content:center;font-weight:700;text-decoration:none;color:inherit}
.tabbar a.active{background:var(--lime);color:var(--ink)}
.tabbar svg{margin-bottom:12px}

/* ways */
.step{left:0;width:100%}
.step.strong{background:var(--teal)}
.step.soft{background:var(--teal-soft)}
.badge{position:absolute;left:36px;width:54px;height:54px;border-radius:50%;background:var(--purple);color:var(--white);font-size:22px;display:flex;align-items:center;justify-content:center}
.step h2{position:absolute;left:36px;font-size:22px;font-weight:700;letter-spacing:.3px}
.step p{position:absolute;left:36px;right:30px;font-size:18px;line-height:24px}
.field{position:absolute;left:36px;width:476px;height:59px;background:var(--white);display:flex;align-items:center;justify-content:space-between;padding:0 22px 0 23px;font-style:italic;font-size:17px;color:#333}
.share-row{position:absolute;left:40px;top:212px;display:flex;gap:17px;align-items:center}
.share-row span{width:56px;height:56px;border-radius:50%;background:var(--white);color:var(--purple);display:flex;align-items:center;justify-content:center}
.learn{position:absolute;left:414px;top:222px;font-size:18px;text-decoration:underline}

/* shop */
.searchbox{left:23px;top:86px;width:501px;height:51px;border:2px solid var(--purple);display:flex;align-items:center;padding:0 16px 0 21px;font-size:15px}
.searchbox .tools{margin-left:auto;display:flex;gap:14px}
.shop-btn{top:156px;width:245px;height:52px;background:var(--purple);color:var(--white);font-size:17px;font-weight:500;display:flex;align-items:center;justify-content:center}
.learn-line{left:0;width:100%;top:233px;text-align:center;font-size:15px}
.results{left:22px;top:288px;font-size:21px;font-weight:700}
.product{width:241px;height:290px;background:var(--white);box-shadow:0 1px 4px rgba(0,0,0,.08)}
.product .shot{position:absolute;left:0;top:0;width:100%;height:122px;background:radial-gradient(ellipse at 55% 55%,var(--shoe-a),var(--shoe-b))}
.product .add{position:absolute;right:18px;top:106px;width:36px;height:36px;border-radius:50%;background:var(--lime);color:var(--white);display:flex;align-items:center;justify-content:center}
.product .stars{position:absolute;left:17px;top:134px;color:var(--purple);font-size:14px;letter-spacing:1px}
.product .pname{position:absolute;left:17px;top:160px;font-size:17px;line-height:20px;font-weight:500}
.product .price{position:absolute;left:19px;top:210px;font-size:17px;font-weight:500}
.product .price s{font-size:14px;font-weight:400;color:#333;margin-left:10px}
.product .compare{position:absolute;left:19px;top:243px;font-size:14px;display:flex;align-items:center;gap:8px}
.product .compare i{width:16px;height:16px;border:1.5px solid var(--purple);display:block}
</style>
</head>
<body>

<svg width="0" height="0" style="position:absolute" aria-hidden="true">
  <symbol id="i-back" viewBox="0 0 24 24"><path d="M15 4 7 12l8 8"/></symbol>
  <symbol id="i-home" viewBox="0 0 24 24"><path d="M3 11 12 3l9 8v10h-6v-6H9v6H3z" fill="currentColor" stroke="none"/></symbol>
  <symbol id="i-globe" viewBox="0 0 24 24"><circle cx="12" cy="12" r="9"/><path d="M3 12h18M12 3c3 3 3 15 0 18M12 3c-3 3-3 15 0 18M5 7h14M5 17h14"/></symbol>
  <symbol id="i-heart" viewBox="0 0 24 24"><path d="M12 20s-8-5-8-11a4.5 4.5 0 0 1 8-2.6A4.5 4.5 0 0 1 20 9c0 6-8 11-8 11z"/></symbol>
  <symbol id="i-chat" viewBox="0 0 24 24"><path d="M4 4h16v12H9l-5 4z"/><path d="M8 8h8M8 12h6"/></symbol>
  <symbol id="i-cart" viewBox="0 0 24 24"><path d="M2 4h3l2 11h12l2-8H6"/><circle cx="9" cy="19" r="1.5"/><circle cx="17" cy="19" r="1.5"/></symbol>
  <symbol id="i-search" viewBox="0 0 24 24"><circle cx="10.5" cy="10.5" r="6.5"/><path d="m15.5 15.5 5 5"/></symbol>
  <symbol id="i-filter" viewBox="0 0 24 24"><path d="M3 4h18l-7 8v7l-4 2v-9z"/></symbol>
  <symbol id="i-lock" viewBox="0 0 24 24"><rect x="5" y="10" width="14" height="11" rx="1" fill="currentColor"/><path d="M8 10V7a4 4 0 0 1 8 0v3"/></symbol>
  <symbol id="i-up" viewBox="0 0 24 24"><path d="M12 15V3M7 8l5-5 5 5M4 14v6h16v-6"/></symbol>
  <symbol id="i-down" viewBox="0 0 24 24"><path d="M12 9v12M7 16l5 5 5-5M4 10V4h16v6"/></symbol>
  <symbol id="i-share" viewBox="0 0 24 24"><circle cx="18" cy="5" r="2.5" fill="currentColor"/><circle cx="6" cy="12" r="2.5" fill="currentColor"/><circle cx="18" cy="19" r="2.5" fill="currentColor"/><path d="m8 11 8-5M8 13l8 5"/></symbol>
  <symbol id="i-dots" viewBox="0 0 24 24"><circle cx="12" cy="5" r="1.8" fill="currentColor"/><circle cx="12" cy="12" r="1.8" fill="currentColor"/><circle cx="12" cy="19" r="1.8" fill="currentColor"/></symbol>
  <symbol id="i-forward" viewBox="0 0 24 24"><path d="M14 4l7 7-7 7v-4c-6 0-9 2-11 6 0-7 4-12 11-12z" fill="currentColor" stroke="none"/></symbol>
  <symbol id="i-plus" viewBox="0 0 24 24"><path d="M12 4v16M4 12h16"/></symbol>
  <symbol id="i-grid" viewBox="0 0 24 24"><g fill="currentColor" stroke="none"><circle cx="4" cy="4" r="2.2"/><circle cx="12" cy="4" r="2.2"/><circle cx="20" cy="4" r="2.2"/><circle cx="4" cy="12" r="2.2"/><circle cx="12" cy="12" r="2.2"/><circle cx="20" cy="12" r="2.2"/><circle cx="4" cy="20" r="2.2"/><circle cx="12" cy="20" r="2.2"/><circle cx="20" cy="20" r="2.2"/></g></symbol>
</svg>

<!-- Profile, compact -->
<section class="screen" style="left:71px;top:91px;width:430px;height:820px">
  <header class="app-header" style="height:63px">
    <svg class="icon back" style="margin-left:6px;width:22px;height:22px"><use href="#i-back"/></svg>
    <h1 style="font-size:16px;margin-left:8px">MY PROFILE</h1>
    <span class="header-avatar" role="img" aria-label="User avatar photo" style="left:389px;top:20px;width:30px;height:30px"></span>
  </header>
  <div class="lavender" style="top:63px;height:254px"></div>
  <div class="avatar" role="img" aria-label="Profile photo" style="left:8px;top:92px;width:66px;height:66px"></div>
  <div style="left:96px;top:104px;font-size:15px;line-height:20px"><div class="name">THEO MARLOW</div><div>@theomarlow</div></div>
  <div class="edit" style="left:340px;top:107px;width:67px;height:34px;font-size:14px">EDIT</div>
  <div class="stat" style="left:5px;top:186px;width:133px;height:95px;font-size:14px"><b style="font-size:19px;margin-bottom:10px">1</b>Price Drop</div>
  <div class="stat" style="left:149px;top:186px;width:133px;height:95px;font-size:14px"><b style="font-size:19px;margin-bottom:10px">0</b>Coupons</div>
  <div class="stat" style="left:293px;top:186px;width:137px;height:95px;font-size:14px"><b style="font-size:19px;margin-bottom:10px">20</b>Earn Cash Back</div>
  <nav class="tabs" style="top:317px;height:45px;font-size:13px"><div class="tab-on" style="width:225px">MY WISHLISTS</div><div class="tab-off">JOINED WISHLISTS</div></nav>
  <div class="wishlist-card" role="img" aria-label="Birthday cake with candles" style="left:3px;top:385px;width:205px;height:178px">
    <span class="members" style="top:12px;padding:3px 8px;font-size:12px">1 member</span>
    <svg class="icon lock" style="right:10px;top:10px;width:20px;height:22px"><use href="#i-lock"/></svg>
    <span class="title" style="left:15px;bottom:12px;font-size:15px">Default Wishlist</span>
  </div>
  <nav class="tabbar" style="height:90px;grid-template-columns:78px repeat(4,1fr);font-size:13px">
    <a class="active"><svg class="icon" width="26" height="26"><use href="#i-home"/></svg>HOME</a>
    <a><svg class="icon" width="26" height="26"><use href="#i-globe"/></svg>DISCOVER</a>
    <a><svg class="icon" width="26" height="26"><use href="#i-heart"/></svg>WISHLIST</a>
    <a><svg class="icon" width="26" height="26"><use href="#i-chat"/></svg>CHAT</a>
    <a><svg class="icon" width="26" height="26"><use href="#i-cart"/></svg>SHOP</a>
  </nav>
</section>

<!-- Profile -->
<section class="screen" style="left:320px;top:58px;width:552px;height:981px">
  <header class="app-header" style="height:61px">
    <svg class="icon back"><use href="#i-back"/></svg>
    <h1>MY PROFILE</h1>
    <span class="header-avatar" role="img" aria-label="User avatar photo" style="left:488px;top:11px;width:38px;height:38px"></span>
  </header>
  <div class="lavender" style="top:61px;height:309px"></div>
  <div class="avatar" role="img" aria-label="Profile photo" style="left:25px;top:96px;width:82px;height:82px"></div>
  <div style="left:134px;top:111px;font-size:19px;line-height:24px"><div class="name">THEO MARLOW</div><div>@theomarlow</div></div>
  <div class="edit" style="left:429px;top:115px;width:81px;height:42px;font-size:18px">EDIT</div>
  <div class="stat" style="left:22px;top:211px;width:163px;height:115px;font-size:18px"><b style="font-size:24px;margin-bottom:10px">1</b>Price Drop</div>
  <div class="stat" style="left:197px;top:211px;width:163px;height:115px;font-size:18px"><b style="font-size:24px;margin-bottom:10px">0</b>Coupons</div>
  <div class="stat" style="left:372px;top:211px;width:163px;height:115px;font-size:18px"><b style="font-size:24px;margin-bottom:10px">20</b>Earn Cash Back</div>
  <nav class="tabs" style="top:370px;height:55px;font-size:17px"><div class="tab-on" style="width:289px">MY WISHLISTS</div><div class="tab-off">JOINED WISHLISTS</div></nav>
  <div class="wishlist-card" role="img" aria-label="Birthday cake with candles" style="left:21px;top:452px;width:248px;height:216px">
    <span class="members" style="top:14px;padding:4px 8px;font-size:15px">1 member</span>
    <svg class="icon lock" style="right:12px;top:12px;width:24px;height:28px"><use href="#i-lock"/></svg>
    <span class="title" style="left:18px;bottom:14px;font-size:20px">Default Wishlist</span>
  </div>
  <nav class="tabbar" style="height:109px;grid-template-columns:112px repeat(4,1fr);font-size:16px">
    <a class="active"><svg class="icon" width="34" height="34"><use href="#i-home"/></svg>HOME</a>
    <a><svg class="icon" width="34" height="34"><use href="#i-globe"/></svg>DISCOVER</a>
    <a><svg class="icon" width="34" height="34"><use href="#i-heart"/></svg>WISHLIST</a>
    <a><svg class="icon" width="34" height="34"><use href="#i-chat"/></svg>CHAT</a>
    <a><svg class="icon" width="34" height="34"><use href="#i-cart"/></svg>SHOP</a>
  </nav>
</section>

<!-- 3 Ways to Find Products -->
<section class="screen" style="left:608px;top:58px;width:552px;height:981px">
  <header class="app-header" style="height:61px">
    <svg class="icon back"><use href="#i-back"/></svg>
    <h1>3 Ways to Find Products</h1>
  </header>
  <div class="step strong" style="top:61px;height:261px">
    <span class="badge" style="top:22px">01</span>
    <h2 style="top:92px">SEARCH FOR PRODUCTS</h2>
    <p style="top:124px">Find products the traditional way with the search bar.</p>
    <div class="field" style="top:170px">Find what you’re looking for<svg class="icon" width="26" height="26" style="color:var(--ink)"><use href="#i-search"/></svg></div>
  </div>
  <div class="step soft" style="top:322px;height:290px">
    <span class="badge" style="top:29px">02</span>
    <h2 style="top:104px">SAVE PRODUCTS FROM APP OR WEBSITE</h2>
    <p style="top:136px;right:56px">Use the share button on other retailer sites or apps to save items to your Pelvosta WishList.</p>
    <div class="share-row">
      <span><svg class="icon" width="26" height="26"><use href="#i-up"/></svg></span>
      <span><svg class="icon" width="26" height="26"><use href="#i-down"/></svg></span>
      <span><svg class="icon" width="26" height="26"><use href="#i-share"/></svg></span>
      <span><svg class="icon" width="26" height="26"><use href="#i-dots"/></svg></span>
      <span><svg class="icon" width="26" height="26"><use href="#i-forward"/></svg></span>
    </div>
    <span class="learn">Learn More</span>
  </div>
  <div class="step strong" style="top:612px;height:262px">
    <span class="badge" style="top:23px">03</span>
    <h2 style="top:94px">FIND PRODUCT BY URL</h2>
    <p style="top:126px;line-height:22px">Visit your favorite stores online and copy and paste the product URL.</p>
    <div class="field" style="top:185px">Paste Product URL<svg class="icon" width="26" height="26" style="color:var(--ink)"><use href="#i-search"/></svg></div>
  </div>
  <nav class="tabbar" style="height:107px;grid-template-columns:repeat(5,1fr);font-size:16px">
    <a><svg class="icon" width="34" height="34"><use href="#i-home"/></svg>HOME</a>
    <a><svg class="icon" width="34" height="34"><use href="#i-globe"/></svg>DISCOVER</a>
    <a><svg class="icon" width="34" height="34"><use href="#i-heart"/></svg>WISHLIST</a>
    <a><svg class="icon" width="34" height="34"><use href="#i-chat"/></svg>CHAT</a>
    <a><svg class="icon" width="34" height="34"><use href="#i-cart"/></svg>SHOP</a>
  </nav>
</section>

<!-- Shop -->
<section class="screen" style="left:897px;top:55px;width:552px;height:981px">
  <header class="app-header" style="height:62px">
    <svg class="icon back"><use href="#i-back"/></svg>
    <h1>Shop</h1>
    <svg class="icon" style="position:absolute;left:512px;top:19px;width:22px;height:22px"><use href="#i-grid"/></svg>
  </header>
  <div class="searchbox">SEARCH<span class="tools"><svg class="icon" width="22" height="22"><use href="#i-search"/></svg><svg class="icon" width="22" height="22"><use href="#i-filter"/></svg></span></div>
  <div class="shop-btn" style="left:23px">FAVORITE BRANDS</div>
  <div class="shop-btn" style="left:283px">PASTE URL</div>
  <div class="learn-line">Learn More : 3 Ways to Save Products</div>
  <h2 class="results">SEARCH RESULTS</h2>

  <article class="product" style="left:23px;top:334px">
    <div class="shot" role="img" aria-label="White high top sneaker on blue backdrop"></div>
    <span class="add"><svg class="icon" width="24" height="24" style="stroke-width:3"><use href="#i-plus"/></svg></span>
    <span class="stars">★★★★★</span>
    <span class="pname">Veldro High Top Mens<br>Fashion Sneakers</span>
    <span class="price">Now $109<s>$129.99</s></span>
    <label class="compare"><i></i>Compare</label>
  </article>
  <article class="product" style="left:284px;top:334px">
    <div class="shot" role="img" aria-label="White high top sneaker on blue backdrop"></div>
    <span class="add"><svg class="icon" width="24" height="24" style="stroke-width:3"><use href="#i-plus"/></svg></span>
    <span class="stars">★★★★★</span>
    <span class="pname">Veldro High Top Mens<br>Fashion Sneakers</span>
    <span class="price">Now $109<s>$129.99</s></span>
    <label class="compare"><i></i>Compare</label>
  </article>
  <article class="product" style="left:22px;top:634px">
    <div class="shot" role="img" aria-label="White high top sneaker on blue backdrop"></div>
    <span class="add"><svg class="icon" width="24" height="24" style="stroke-width:3"><use href="#i-plus"/></svg></span>
    <span class="stars">★★★★★</span>
    <span class="pname">Veldro High Top Mens<br>Fashion Sneakers</span>
    <span class="price">Now $109<s>$129.99</s></span>
  </article>
  <article class="product" style="left:284px;top:634px">
    <div class="shot" role="img" aria-label="White high top sneaker on blue backdrop"></div>
    <span class="add"><svg class="icon" width="24" height="24" style="stroke-width:3"><use href="#i-plus"/></svg></span>
    <span class="stars">★★★★★</span>
    <span class="pname">Veldro High Top Mens<br>Fashion Sneakers</span>
    <span class="price">Now $109<s>$129.99</s></span>
  </article>

  <nav class="tabbar" style="height:109px;grid-template-columns:117px repeat(4,1fr);font-size:16px">
    <a class="active"><svg class="icon" width="34" height="34"><use href="#i-home"/></svg>HOME</a>
    <a><svg class="icon" width="34" height="34"><use href="#i-globe"/></svg>DISCOVER</a>
    <a><svg class="icon" width="34" height="34"><use href="#i-heart"/></svg>WISHLIST</a>
    <a><svg class="icon" width="34" height="34"><use href="#i-chat"/></svg>CHAT</a>
    <a><svg class="icon" width="34" height="34"><use href="#i-cart"/></svg>SHOP</a>
  </nav>
</section>

</body>
</html>
```